Leadership Brenvale Brochure Design*

We host a local leadership development program every two years. We need a brochure to promote the program. We would like it to be 8 1/2 x 11, tri-fold. I have attached a Word document with the necessary info for the brochure. The brochure will be professionally printed. We would like the final design to be in InDesign.

Target Market(s)

Potential participants of our leadership program. They will be local leaders, male and female, from 30-60 years of age.

Requirements
Must have
• Content as detailed in the Word document attached. Our logo.
Nice to have
• A design that is attractive to young professionals.

```html
<!DOCTYPE html>
<html lang="en">
<head>
<meta charset="utf-8">
<title>Leadership Brenvale Brochure</title>
<link href="https://fonts.googleapis.com/css2?family=Lato:ital,wght@0,300;0,400;0,700;0,900;1,300;1,400;1,700&display=swap" rel="stylesheet">
<style>
:root{
  --green:#55f32a;
  --tick:#4fe02c;
  --time:#52d83a;
  --royal:#1f3fe8;
  --ink:#1f3fd0;
  --cyan:#3fc9ee;
  --sky:#4fd8f8;
  --white:#ffffff;
}
*{margin:0;padding:0;box-sizing:border-box}
html,body{width:848px;height:1200px;overflow:hidden;background:#fff}
body{font-family:'Lato',sans-serif;position:relative;color:var(--ink)}
.spread{position:absolute;left:105px;width:642px;height:474px;background:#fff;box-shadow:0 6px 10px rgba(0,0,0,.12)}
.spread--outside{top:67px}
.spread--inside{top:579px}
.col{position:absolute;top:0;height:100%}

/* outside */
.testimonials{left:0;width:214px;background:var(--green);padding:21px 17px 0 17px;color:var(--white)}
.testimonials h2{font-size:9px;font-weight:700;color:#2f7dfa;margin-bottom:7px}
.quote{font-size:7.6px;font-style:italic;font-weight:300;line-height:12.3px}
.attribution{font-size:8px;font-weight:400;text-align:right;line-height:12.3px;margin:10px 0 24px}
.details{left:214px;width:214px;padding:21px 14px 0 17px}
.details h3{font-size:9px;font-weight:700;color:var(--cyan);margin-bottom:4px}
.details p{font-size:8px;line-height:12.4px;margin-bottom:12px}
.details strong{font-weight:900;color:var(--royal)}
.call{text-align:center;color:var(--cyan);font-weight:700;font-size:9px;line-height:16px;margin-top:-1px}
.mini-mark{display:flex;align-items:center;justify-content:center;gap:4px;margin-top:12px;font-size:7px;font-weight:900;color:var(--royal);text-transform:uppercase}
.dot{width:10px;height:10px;border-radius:50%;background:var(--cyan);display:inline-block}
.cover{left:428px;width:214px}
.cover__quote{height:237px;background:var(--royal);color:var(--white);font-style:italic;font-weight:700;font-size:10.6px;line-height:14px;text-align:center;padding:82px 18px 0}
.cover__name{display:flex;align-items:center;justify-content:center;gap:7px;margin-top:68px;color:var(--royal);font-weight:900;font-size:17px;line-height:18px;text-transform:uppercase}
.cover__name .dot{width:26px;height:26px;background:#f58a35}
.sponsors{text-align:center;font-size:8px;line-height:14px;margin-top:72px}
.sponsors b{font-weight:700;display:block}

/* inside */
.intro{position:absolute;left:0;top:0;width:428px;height:132px;background:var(--sky);color:var(--white);padding:24px 17px 0;font-weight:700;font-size:9.6px;line-height:15.5px}
.intro .brand{font-size:12px}
.intro p+p{margin-top:6px}
.goals{position:absolute;left:12px;top:150px;width:190px;list-style:none}
.goals li{display:flex;gap:7px;color:var(--cyan);font-weight:700;font-size:9.6px;line-height:15.5px;margin-bottom:10px}
.goals svg{flex:none;margin-top:6px}
.photo{position:absolute;left:0;top:347px;width:214px;height:127px;background:linear-gradient(180deg,#b9a483 0%,#8e7a62 55%,#5b5350 100%)}
.schedule{position:absolute;left:226px;top:146px;width:200px}
.schedule h2{font-size:10.5px;font-weight:700;color:var(--time);margin-bottom:6px}
.event{display:flex;gap:6px;margin-bottom:12px}
.event__date{width:36px;flex:none;text-align:center;color:var(--time);font-size:11.5px;line-height:15px}
.event__body{font-size:7.6px;line-height:12.4px}
.event__title{font-weight:700;font-size:8.6px}
.event__time{color:var(--time)}
.schedule-cont{position:absolute;left:440px;top:28px;width:196px}
.invite{position:absolute;left:428px;top:391px;width:214px;height:83px;background:var(--royal);color:var(--white);font-weight:700;font-size:8.2px;line-height:12.5px;text-align:center;padding:20px 10px 0}
</style>
</head>
<body>

<section class="spread spread--outside">
  <div class="col testimonials">
    <h2>What Community alumni are saying</h2>
    <p class="quote">“Leadership Brenvale was an awesome experience! I learned many interesting things about the county that I have lived in all my life. We had very informative panel discussions and the tours of local attractions, including the Harlow Ridge Correctional Facility were eye opening! I enjoyed learning and working beside a great group of folks who are taking leadership roles in our communities to make our county a better place to live, work and play.”</p>
    <p class="attribution">Dana Whitfield, Co-Owner, Smokehouse 41</p>
    <p class="quote">“For the first year and a half I was working at R. Calder Hayes, I commuted from Port Ellis, so I was not involved in the community at all. Once we moved here, I knew I wanted and felt I had to become more involved. I learned about the program through a colleague. I couldn’t have asked for a better experience and it really exposed me to the many ways that I could get involved and contribute to the chamber and our community. I didn’t know a soul in that 2014 class when it started and now many of them are my very best friends. If you have an opportunity to go through Leadership Brenvale you would be crazy to pass it up. It is the best program the Chamber has and, quite frankly, one of the best opportunities to better yourself in this community.”</p>
    <p class="attribution">Owen T. Barrett, CPA,<br>Partner/Manager of the Marston Office R.<br>Calder Hayes &amp; Associates, LLP</p>
  </div>

  <div class="col details">
    <h3>Attendance Policy</h3>
    <p>Attendance at all sessions including the opening retreat is compulsory. Participants may miss no more than one session to graduate; however, the <strong>Organizational Retreat is mandatory</strong>.</p>
    <h3>Tuition</h3>
    <p>If accepted in the Leadership Brenvale program, you or your employer/sponsor will be invoiced $400 for Chamber members and $500 for non-members. This fee covers costs for the retreat, classroom sessions, lunches, and graduation. No refunds will be provided for participants who drop out of the program or do not fulfill the required curriculum.</p>
    <h3>To Apply</h3>
    <p>Applications are available on the Chamber’s website, <strong>www.TheBrenvaleChamber.com</strong> Applications are due by November 2, 2020.</p>
    <p>Class size is limited. All applications received by the deadline will be reviewed and final participants for the Leadership Brenvale class will be contacted on December 4, 2020. However, all applicants will be notified of the status of their application in writing.</p>
    <p class="call">For questions, please call the Chamber<br>555-014-2290</p>
    <div class="mini-mark"><span class="dot"></span>Leadership Brenvale</div>
  </div>

  <div class="col cover">
    <div class="cover__quote">“The greatest wealth of a community lies not in the amount of its treasure, but in the quality of its leadership.”</div>
    <div class="cover__name"><span class="dot"></span><span>Leadership<br>Brenvale</span></div>
    <p class="sponsors"><b>SPONSORED BY</b>Eastfield Community College<br>Brenvale Chamber of Commerce and Tourism</p>
  </div>
</section>

<section class="spread spread--inside">
  <div class="intro">
    <p><span class="brand">Leadership Brenvale</span> is a leadership certification program designed to prepare the leaders of tomorrow. During the five-month program, participants get an in-depth view of community issues, develop leadership skills necessary to assume leadership roles, and are exposed to community involvement opportunities.</p>
    <p>Leadership Brenvale will provide participants with the opportunities to:</p>
  </div>

  <ul class="goals">
    <li><svg width="14" height="20" viewBox="0 0 14 20"><path d="M1 11 L5 19 L13 1" fill="none" stroke="#4fe02c" stroke-width="1.6"/></svg>Build and demonstrate leadership and communication skills</li>
    <li><svg width="14" height="20" viewBox="0 0 14 20"><path d="M1 11 L5 19 L13 1" fill="none" stroke="#4fe02c" stroke-width="1.6"/></svg>Establish ongoing dialogues with experienced community leaders</li>
    <li><svg width="14" height="20" viewBox="0 0 14 20"><path d="M1 11 L5 19 L13 1" fill="none" stroke="#4fe02c" stroke-width="1.6"/></svg>Build meaningful, long-lasting connections</li>
    <li><svg width="14" height="20" viewBox="0 0 14 20"><path d="M1 11 L5 19 L13 1" fill="none" stroke="#4fe02c" stroke-width="1.6"/></svg>Think critically about key business, policy, and civic issues facing Brenvale County</li>
  </ul>

  <div class="photo" role="img" aria-label="Group photo of a past leadership class standing together in a meeting room"></div>

  <div class="schedule">
    <h2>Schedule</h2>
    <div class="event"><div class="event__date">17<br>Jan</div><div class="event__body"><div class="event__title">Organizational Retreat &amp; Dinner</div>(Attendance Mandatory)<br><span class="event__time">10:00 a.m. – 7:00 p.m.</span><br>Introductions<br>Team Building<br>Motivation<br>Leadership Styles<br>Social Hour/Dinner</div></div>
    <div class="event"><div class="event__date">31<br>Jan</div><div class="event__body"><div class="event__title">Business &amp; Industry</div><span class="event__time">8:30 a.m. – 4:00 p.m.</span><br>Business &amp; Industry Panel<br>Tour of Tellmark Manufacturing facility<br>Tour of Ridgeway Tool Company<br>“Taking your vision into B&amp;I”</div></div>
    <div class="event"><div class="event__date">21<br>Feb</div><div class="event__body"><div class="event__title">Education</div><span class="event__time">8:30 a.m. – 4:00 p.m.</span><br>Tour of selected programs at ECC<br>College Career Program overview<br>Lunch at Brenvale Career &amp; College Academy<br>Tour of BCCA<br>Overview of CTE program paths</div></div>
  </div>

  <div class="schedule-cont">
    <div class="event"><div class="event__date">14<br>Mar</div><div class="event__body"><div class="event__title">Future Technologies &amp;<br>Communications</div><span class="event__time">8:30 a.m. – 4:00 p.m.</span><br>ECC Presents interview<br>Trends and forecasts<br>Marketing &amp; communications panel</div></div>
    <div class="event"><div class="event__date">4<br>Apr</div><div class="event__body"><div class="event__title">Government</div><span class="event__time">8:30 a.m. – 4:00 p.m.</span><br>Overview of state/federal government<br>Overview of city/county government<br>Tour of Harlow Ridge Correctional Institute<br>Tour of courthouse<br>Judicial presentations</div></div>
    <div class="event"><div class="event__date">2<br>May</div><div class="event__body"><div class="event__title">Health &amp; Wellness</div><span class="event__time">8:30 a.m. – 4:00 p.m.</span><br>Tour of Riverbend Hospice<br>Community Wellness Roundtable<br>Tour of Alston Cancer Care Center<br>Virtual Medicine Tutorial<br>Tour of BRHS</div></div>
    <div class="event"><div class="event__date">18<br>May</div><div class="event__body"><div class="event__title">Graduation Ceremony and<br>Luncheon</div><span class="event__time">12:00 p.m.</span></div></div>
  </div>

  <div class="invite">Participants are encouraged to invite their employer/supervisor/mentor/special guest (x2)</div>
</section>

</body>
</html>
```